New Office Poster Designs

Attached you will find 3 poster designs that we found online along with our logos. Please use our logos to reference any type of color or design.
These posters will be hung around our Loan Offices.

INSTRUCTIONS: Please mimic all 3 posters (MINUS THE SMALL WRITING ON THEM THAT IS NOT IN ENGLISH IGNORE THAT)
but use our logos and colors. Also, if you can make them in Spanish as well as English that is a plus. We will also need 1 additional poster with the below wording.

Additional Poster:
Stuck in a Title Loan? Let us pay it off up to $10,000

Target Market(s)

People looking to get a loan and need money

Industry/Entity Type

Loan Industry - Consumer Lending - Fast easy loans

Requirements
Nice to have
• English and Spanish

```html
<!DOCTYPE html>
<html lang="en">
<head>
<meta charset="utf-8">
<title>Loan Office Posters – English and Spanish</title>
<link rel="stylesheet" href="https://fonts.googleapis.com/css2?family=Poppins:wght@400;500;700&family=Montserrat:wght@700&display=swap">
<style>
  :root {
    --page-bg: #e4e4e4;
    --paper: #ffffff;
    --green-light: #2f8a5d;
    --green-mid: #237049;
    --green-dark: #124a2e;
    --green-deep: #0c3a22;
    --brand-red: #c8202a;
    --text-white: #ffffff;
    --label-grey: #5a5a5a;
  }
  * { box-sizing: border-box; margin: 0; padding: 0; }
  html, body {
    width: 1200px; height: 885px; overflow: hidden;
    background: var(--page-bg);
    font-family: "Poppins", sans-serif;
  }
  .stage { position: relative; width: 1200px; height: 885px; }

  .poster {
    position: absolute; top: 159px;
    width: 410px; height: 574px;
    background: var(--paper);
    padding: 8px;
  }
  .poster--english { left: 134px; }
  .poster--spanish { left: 664px; }

  .poster__sheet {
    position: relative; width: 100%; height: 100%;
    overflow: hidden; color: var(--text-white);
  }
  .poster__money-top {
    position: absolute; left: 0; top: 0; width: 100%; height: 203px;
    background: linear-gradient(160deg, var(--green-light), var(--green-mid));
  }
  .poster__money-bottom {
    position: absolute; left: 0; top: 203px; width: 100%; bottom: 0;
    background: linear-gradient(170deg, var(--green-dark), var(--green-deep));
  }
  .poster__frame {
    position: absolute; left: 12px; top: 11px; right: 10px; bottom: 11px;
    border: 1px solid rgba(255,255,255,0.85);
  }

  .headline {
    position: absolute; left: 0; right: 0; top: 44px;
    text-align: center; line-height: 1;
    text-shadow: 0 3px 4px rgba(0,0,0,0.35);
  }
  .headline__lead { display: block; font-weight: 500; font-size: 60px; letter-spacing: -1px; }
  .headline__amount { display: block; font-weight: 700; font-size: 62px; margin-top: 0; letter-spacing: -1px; }

  .dollars {
    position: absolute; left: 0; right: 0; top: 240px;
    display: flex; justify-content: center; align-items: flex-end; gap: 18px;
    font-weight: 700; line-height: 1;
    text-shadow: 0 3px 5px rgba(0,0,0,0.35);
  }
  .dollars__small { font-size: 84px; }
  .dollars__large { font-size: 104px; position: relative; top: -22px; }

  .smile-curve { position: absolute; left: 0; top: 0; width: 394px; height: 558px; }

  .brand-block {
    position: absolute; left: 259px; top: 383px;
    width: 87px; height: 87px; background: var(--brand-red);
    display: flex; align-items: center; justify-content: center;
    font-weight: 500; font-size: 15px; color: var(--text-white);
  }

  .offer-note {
    position: absolute; left: 46px; top: 421px;
    font-weight: 400; font-size: 19px; line-height: 1;
  }
  .offer-phone {
    position: absolute; left: 46px; top: 447px;
    font-weight: 700; font-size: 23px; line-height: 1; letter-spacing: 0.3px;
  }
  .contact-rule {
    position: absolute; left: 49px; top: 485px; width: 178px;
    border-top: 1px solid rgba(255,255,255,0.9);
  }
  .contact-web {
    position: absolute; right: 47px; top: 477px;
    font-size: 12px; line-height: 1;
  }
  .contact-web strong { font-weight: 700; }
  .fine-print {
    position: absolute; left: 49px; right: 47px; top: 498px;
    font-size: 5.6px; line-height: 1.3; text-align: justify;
  }

  .poster-label {
    position: absolute; top: 792px; width: 410px;
    text-align: center;
    font-family: "Montserrat", sans-serif; font-weight: 700;
    font-size: 23px; color: var(--label-grey); letter-spacing: 0.5px;
  }
  .poster-label--english { left: 134px; }
  .poster-label--spanish { left: 664px; }
</style>
</head>
<body>
<main class="stage">

  <section class="poster poster--english" lang="en">
    <div class="poster__sheet">
      <div class="poster__money-top" role="img" aria-label="Scattered dollar bills tinted green"></div>
      <div class="poster__money-bottom" role="img" aria-label="Scattered dollar bills tinted dark green"></div>
      <div class="poster__frame"></div>
      <h1 class="headline">
        <span class="headline__lead">GET UP TO</span>
        <span class="headline__amount">$10,000</span>
      </h1>
      <div class="dollars" aria-hidden="true">
        <span class="dollars__small">$</span><span class="dollars__large">$</span><span class="dollars__small">$</span>
      </div>
      <svg class="smile-curve" viewBox="0 0 394 558" aria-hidden="true">
        <path d="M85 387 Q205 320 309 375 Q200 345 85 387 Z" fill="var(--brand-red)"/>
      </svg>
      <div class="brand-block">Ledgerly</div>
      <p class="offer-note">Limited time</p>
      <p class="offer-phone">0198-765-432</p>
      <div class="contact-rule"></div>
      <p class="contact-web">www.<strong>ledgerly</strong>.com</p>
      <p class="fine-print">Loan approval depends on income verification and credit review. Rates, fees and terms vary by applicant, loan amount and location. Funds may be available the same business day once approved. Please bring a valid photo ID, proof of income, a recent utility bill and your vehicle title if you have one. Late payments may result in additional fees. Visit any of our offices or call our friendly team to learn more about your options today, with no obligation.</p>
    </div>
  </section>

  <section class="poster poster--spanish" lang="es">
    <div class="poster__sheet">
      <div class="poster__money-top" role="img" aria-label="Billetes de dólar esparcidos en tono verde"></div>
      <div class="poster__money-bottom" role="img" aria-label="Billetes de dólar esparcidos en tono verde oscuro"></div>
      <div class="poster__frame"></div>
      <h1 class="headline">
        <span class="headline__lead">LLEGAR A</span>
        <span class="headline__amount">$10,000</span>
      </h1>
      <div class="dollars" aria-hidden="true">
        <span class="dollars__small">$</span><span class="dollars__large">$</span><span class="dollars__small">$</span>
      </div>
      <svg class="smile-curve" viewBox="0 0 394 558" aria-hidden="true">
        <path d="M85 387 Q205 320 309 375 Q200 345 85 387 Z" fill="var(--brand-red)"/>
      </svg>
      <div class="brand-block">Ledgerly</div>
      <p class="offer-note">Tiempo limitado</p>
      <p class="offer-phone">0198-765-432</p>
      <div class="contact-rule"></div>
      <p class="contact-web">www.<strong>ledgerly</strong>.com</p>
      <p class="fine-print" lang="en">Loan approval depends on income verification and credit review. Rates, fees and terms vary by applicant, loan amount and location. Funds may be available the same business day once approved. Please bring a valid photo ID, proof of income, a recent utility bill and your vehicle title if you have one. Late payments may result in additional fees. Visit any of our offices or call our friendly team to learn more about your options today, with no obligation.</p>
    </div>
  </section>

  <p class="poster-label poster-label--english">ENGLISH</p>
  <p class="poster-label poster-label--spanish">SPANISH</p>

</main>
</body>
</html>
```